An magic noodle needs an packing and logo design

We need a packing and logo design for an amazing noodle named Slurpio, which is a series of low-calorie noodles with zero net carbs are made out of water-soluble dietary fiber made from the natural Konjac. Not only are they yummy, but Slurpio are able to satisfy your hunger just like regular noodles and you will find yourself losing weight magically with enjoying delicious food.
Updates

Project Deadline Extended Reason: Some designer applied awaiting and said their design will come soon. Added Wednesday, July 12, 2017

Target Market(s)

Somebody who seeks a healthy and yummy meal to keep fit or lose weight.

Logo Text

Slurpio

Requirements
Must have
• The front side:
• Logo
• Low-calorie, Low-carb, Low Cholesterol, Gluten free, Good Source of Fiber, Gluten Free, Dairy Free, NON-GMO
• 纯天然高纤低脂面
• Tomato flavor, 68 Cal
• Ready to enjoy 1 min, Pre-cooked meal
• A brief description for Konjac glucomannan (Konjac glucomannan is the best natural soluble dietary fiber.
• The Northfield Nutrition Council recommends a healthy diet including 25-38 grams of fiber per day.)
• The back side:
• Storage instructions
• Cooking instructions
• The story: Konjac, which is also called “Moyu”, “Juro” or “Shirataki”, belongs to Araceae, and it’s the only perennial plant that can provide a large amount of glucomannan. Konjac fiber, as known as glucomannan, is a kind of good water-soluble dietary fiber, and is given the name of “The seventh nutrient”, “Blood purification agent”.
• The beneficial dietary fiber derived from the organic Konjac root, which is native to Asia, especially Shaanxi of China, where is the home of wild giant pandas and is richly endowed with varied landforms and a complex ecosystem containing many rare animals and plants. This national nature reserve has been described as the “Natural Animal and Plant Gene Base”.)
• Nutrition Facts
• The dimension of old vision is 380*195mm and the material will be aluminum foil. But the dimension is adjustable if the designer has a better opinion. The food in the packaging is one meal. I have uploaded the previous packaging and the one from the same industry.
Nice to have
• The figure of great panda

```html
<!DOCTYPE html>
<html lang="en">
<head>
<meta charset="UTF-8">
<title>Slurpio – Konjac 3D noodles, Tomato flavor</title>
<link rel="stylesheet" href="https://fonts.googleapis.com/css2?family=Didact+Gothic&family=Zilla+Slab:wght@300&family=PT+Sans&display=swap">
<style>
  :root {
    --ink: #000000;
    --paper: #ffffff;
    --konjac-green: #2e8b3e;
    --leaf-green: #d6e9b4;
    --tomato: #f06a6f;
    --frame: #1a1a1a;
  }
  * { margin: 0; padding: 0; box-sizing: border-box; }
  html, body {
    width: 1171px; height: 1200px; overflow: hidden;
    background: var(--paper);
  }
  .package-front {
    position: relative;
    width: 1171px; height: 1200px;
    background: var(--paper);
    font-family: "Didact Gothic", sans-serif;
  }
  .package-frame {
    position: absolute;
    left: 18px; top: 17px; width: 1124px; height: 1155px;
    border: 2px solid var(--frame);
  }
  .brand-bar {
    position: absolute;
    left: 349px; top: 19px; width: 461px; height: 187px;
    background: var(--ink);
    display: flex; align-items: center; justify-content: center; gap: 22px;
  }
  .brand-dot {
    width: 46px; height: 46px; border-radius: 50%;
    border: 4px solid var(--paper);
  }
  .brand-name {
    font-family: "Didact Gothic", sans-serif;
    color: var(--paper);
    font-size: 86px; line-height: 1;
  }
  .leaf-spray {
    position: absolute;
    left: 298px; top: 245px; width: 590px; height: 315px;
    background: radial-gradient(ellipse at 50% 55%, var(--leaf-green) 0%, rgba(214,233,180,0.75) 45%, rgba(214,233,180,0) 72%);
  }
  .product-kind {
    position: absolute;
    left: 0; width: 1171px; top: 512px;
    text-align: center;
    font-family: "Didact Gothic", sans-serif;
    color: var(--konjac-green);
    font-size: 66px; line-height: 1; letter-spacing: 2px;
  }
  .product-name {
    position: absolute;
    left: 0; width: 1171px; top: 570px;
    text-align: center;
    font-family: "Zilla Slab", serif;
    font-weight: 300;
    color: var(--ink);
    font-size: 150px; line-height: 1;
  }
  .title-rule {
    position: absolute;
    left: 183px; top: 727px; width: 794px; height: 3px;
    background: var(--ink);
  }
  .claim-icons {
    position: absolute;
    left: 368px; top: 778px;
  }
  .claim-icons svg { display: block; }
  .claim-label {
    font-family: "Didact Gothic", sans-serif;
    fill: var(--konjac-green);
    font-size: 15px;
  }
  .konjac-description {
    position: absolute;
    left: 190px; width: 780px; top: 935px;
    text-align: center;
    font-family: "PT Sans", sans-serif;
    font-size: 21.5px; line-height: 30px;
    color: var(--ink);
  }
  .flavor-band {
    position: absolute;
    left: 349px; top: 1083px; width: 461px; height: 87px;
    background: var(--tomato);
    color: var(--paper);
    display: flex; align-items: center; justify-content: center;
    font-family: "Didact Gothic", sans-serif;
    font-size: 50px;
  }
</style>
</head>
<body>
<main class="package-front">
  <div class="package-frame"></div>

  <header class="brand-bar">
    <span class="brand-dot"></span>
    <span class="brand-name">Slurpio</span>
  </header>

  <div class="leaf-spray" role="img" aria-label="Spray of pale green konjac leaves"></div>

  <p class="product-kind">KONJAC</p>
  <h1 class="product-name">3D noodles</h1>
  <div class="title-rule"></div>

  <div class="claim-icons">
    <svg width="425" height="95" viewBox="0 0 425 95" aria-label="Low cal, good source of fiber, low carb">
      <g fill="none" stroke="#2e8b3e" stroke-width="2.5" stroke-linejoin="miter">
        <path d="M29 3 H72 V44 H97 L50.5 89 L4 44 H29 Z"/>
        <path d="M351 3 H394 V44 H419 L372.5 89 L326 44 H351 Z"/>
        <path d="M150 40 L176 86 L202 8"/>
      </g>
      <text class="claim-label" x="50.5" y="38" text-anchor="middle">LOW</text>
      <text class="claim-label" x="50.5" y="62" text-anchor="middle">CAL</text>
      <text class="claim-label" x="372.5" y="38" text-anchor="middle">LOW</text>
      <text class="claim-label" x="372.5" y="62" text-anchor="middle">CARB</text>
      <text class="claim-label" x="252" y="44" text-anchor="middle">GOOD</text>
      <text class="claim-label" x="248" y="63" text-anchor="middle">SOURCE</text>
      <text class="claim-label" x="242" y="83" text-anchor="middle">OF FIBER</text>
    </svg>
  </div>

  <p class="konjac-description">brief description for Konjac glucomannan brief description for Konjac glucomannan brief description for Konjac glucomannan brief description for Konjac glucomannan</p>

  <div class="flavor-band">Tomato flavor</div>
</main>
</body>
</html>
```